The Maplewick Academy Web Page

We need a web design for our Day Care Center based in Brandon, Florida. We are targeting child care and educational services to middle class parents, specially the mother. We would like to see designs that matches attached logo mark. The final design should communicate higher standards for day care and educational services.

Target Market(s)

Middle class parents in the State of Florida

Coding

Number of Pages Required

5+ page

```html
<!DOCTYPE html>
<html lang="en">
<head>
<meta charset="utf-8">
<title>The Maplewick Academy</title>
<link href="https://fonts.googleapis.com/css2?family=Raleway:wght@400;500;600;700&family=Open+Sans:wght@400;600;700&display=swap" rel="stylesheet">
<style>
:root{
  --navy:#0d2240;
  --gold:#e2b24c;
  --gold-light:#fbe79c;
  --footer-gold:#f2dd92;
  --page:#efefef;
  --white:#ffffff;
  --ink:#333333;
  --muted:#8a8a8a;
  --blue:#5aa9d6;
  --green:#6dbf67;
  --salmon:#ef8b7a;
  --line:#dddddd;
}
*{box-sizing:border-box;margin:0;padding:0}
html,body{width:1200px;height:2667px;overflow:hidden}
body{position:relative;background:var(--page);font-family:"Raleway",sans-serif;color:var(--ink)}
.abs{position:absolute}
.main-nav{left:0;top:0;width:1200px;height:30px;background:var(--navy);display:flex;justify-content:center;gap:30px;align-items:center;font-family:"Open Sans",sans-serif;font-weight:600;font-size:15px;color:var(--white)}
.main-nav .active{color:var(--gold)}
.sub-nav{left:0;top:30px;width:1200px;height:32px;background:var(--gold);display:flex;justify-content:center;gap:26px;align-items:center;font-family:"Open Sans",sans-serif;font-size:12.5px;color:var(--navy)}
.dropdown{left:356px;top:39px;width:167px;height:165px;background:rgba(253,244,205,.95);padding:8px 14px;font-family:"Open Sans",sans-serif;font-size:13px;line-height:26px;color:var(--navy)}
.hero{left:192px;top:85px;width:816px;height:418px;border-radius:4px;overflow:hidden;background:linear-gradient(135deg,#b7d47a 0%,#e9c9a8 45%,#f3d8a2 70%,#e6b86a 100%)}
.hero-title{left:0;top:270px;width:816px;text-align:center;font-size:42px;color:#1a1a1a;font-weight:500}
.hero-sub{left:0;top:322px;width:816px;text-align:center;font-size:13px;color:#222}
.slide-arrow{width:32px;height:32px;background:var(--blue);border-radius:3px}
.crest{left:532px;top:444px;width:136px;height:136px;border-radius:50%;background:var(--navy);border:5px solid var(--white);box-shadow:0 0 0 3px #cfcfcf;display:flex;align-items:center;justify-content:center;text-align:center;color:var(--white);font-size:15px;font-weight:600;line-height:1.25;padding:18px}
h1.welcome{left:0;top:605px;width:1200px;text-align:center;font-size:34px;font-weight:400;color:#333}
.card{width:250px;height:279px;background:var(--white);box-shadow:0 1px 3px rgba(0,0,0,.15);text-align:center;top:674px}
.card .photo{height:181px}
.card h3{font-size:20px;font-weight:600;margin-top:12px}
.card p{font-size:11.5px;color:var(--muted);line-height:16px;padding:6px 22px 0}
.band{left:0;top:981px;width:1200px;height:281px;background:var(--white);border-bottom:2px solid #e4e4e4}
.band h2{position:absolute;left:0;top:26px;width:1200px;text-align:center;font-size:34px;font-weight:400;color:#444}
.service{top:100px;width:250px}
.service .icon{position:absolute;left:0;top:0;width:50px;height:50px;border-radius:4px}
.service h4{position:absolute;left:66px;top:0;font-size:15px;font-weight:500;color:#333;white-space:nowrap}
.service p{position:absolute;left:66px;top:25px;width:184px;font-size:11px;line-height:16px;color:var(--muted)}
.service .btn{position:absolute;left:66px;top:112px}
.btn{display:inline-block;background:var(--blue);color:var(--white);font-size:10px;text-align:center;border-radius:2px;width:71px;height:23px;line-height:23px}
.divider{top:104px;width:1px;height:120px;background:var(--line)}
.program{left:192px;top:1303px;width:565px;height:567px;background:var(--white)}
.program h2{position:absolute;left:28px;top:18px;font-size:30px;font-weight:400}
.program .call{position:absolute;left:28px;top:60px;font-size:14px;color:#444}
.program .call b{color:#111}
.program .photo{position:absolute;left:28px;top:105px;width:500px;height:213px;background:linear-gradient(120deg,#7fae5a,#d9a58a 40%,#c94f4a 65%,#f0d9c0)}
.program h3{position:absolute;left:28px;font-size:15px;font-weight:500}
.program p{position:absolute;left:28px;width:500px;font-size:11.5px;line-height:16px;color:var(--muted)}
.programs-menu{left:757px;top:1303px;width:250px;height:567px;background:var(--gold-light)}
.programs-menu h3{position:absolute;left:32px;top:26px;font-size:20px;font-weight:400;color:#444}
.programs-menu .toggle{position:absolute;left:148px;top:28px;width:22px;height:22px;background:#e9e1c0;border-radius:3px}
.programs-menu ul{position:absolute;left:0;top:72px;width:250px;list-style:none}
.programs-menu li{height:44px;line-height:44px;padding-left:32px;font-size:12px;color:#666}
.programs-menu li.current{background:var(--white);color:#111;font-weight:700}
.tabs{left:192px;top:1908px;width:530px;height:277px;background:var(--white)}
.tab-bar{position:absolute;left:0;top:0;width:530px;height:43px;background:#e6e6e6;display:flex;font-size:12px;color:#777}
.tab-bar span{padding:0 18px;line-height:43px}
.tab-bar .on{background:var(--white);color:#111;width:183px;padding:0 12px}
.tabs .photo{position:absolute;left:30px;top:71px;width:151px;height:146px;border-radius:6px;background:linear-gradient(160deg,#9fc6e0,#d8bf78 55%,#8fb85c)}
.tabs h4{position:absolute;left:215px;top:70px;font-size:15px;font-weight:700}
.tabs p{position:absolute;left:215px;width:290px;font-size:11.5px;line-height:15.5px;color:#666}
.about{left:757px;top:1908px;width:250px;height:277px;background:var(--white)}
.about h3{position:absolute;left:20px;top:12px;width:220px;font-size:20px;font-weight:400;line-height:22px;color:#444}
.about .tag{position:absolute;left:20px;top:66px;font-size:11px;color:#777}
.about .seal{position:absolute;left:20px;top:106px;width:58px;height:58px;border-radius:50%;background:var(--navy)}
.about h4{position:absolute;left:86px;top:112px;font-size:14px;font-weight:500}
.about p{position:absolute;left:86px;top:134px;width:140px;font-size:11px;line-height:14.5px;color:#777}
.footer{left:0;top:2210px;width:1200px;height:386px;background:var(--footer-gold)}
.footer .photo{position:absolute;left:439px;top:0;width:370px;height:386px;background:radial-gradient(circle at 50% 52%,#c9a26a 0%,#b8895a 45%,#e6cf90 100%)}
.footer .crest{left:518px;top:110px;width:164px;height:164px;font-size:18px}
.hours{left:222px;top:34px;width:210px;font-size:15px;line-height:20px;color:#222}
.hours b{font-weight:700}
.hours .ico{position:absolute;left:-22px;width:14px;height:14px}
.contact{left:807px;top:34px;width:200px}
.contact h4{font-size:15px;font-weight:700}
.contact p{font-size:12.5px;line-height:15px;color:#333}
.field{position:absolute;left:0;width:200px;height:27px;background:var(--white);border:1px solid #ddd;font-size:10px;color:#888;padding:5px 6px}
.send{position:absolute;left:0;top:288px;width:87px;height:27px;background:var(--blue);color:var(--white);font-size:10px;line-height:27px;padding-left:18px;border-radius:2px}
.send::after{content:"";position:absolute;left:58px;top:0;width:1px;height:27px;background:rgba(255,255,255,.5)}
.bottom{left:0;top:2596px;width:1200px;height:71px;background:#e9e9e9}
.bottom .copy{position:absolute;left:190px;top:26px;font-size:14px;color:#666}
.social{top:20px;width:30px;height:30px;border-radius:2px}
</style>
</head>
<body>

<nav class="abs main-nav">
  <span>Admissions</span><span class="active">Philosophy</span><span>Programs</span><span>Services</span><span>Campuses</span><span>Franchises</span><span>Business</span><span>Contact</span>
</nav>
<nav class="abs sub-nav">
  <span>Preferred Vendors</span><span>Business Co-Ops</span><span>Career Opportunities</span><span>Privacy Policy</span><span>Franchise</span><span>Privacy Policy</span>
</nav>

<section class="abs hero" role="img" aria-label="Photo of a smiling teacher with a group of young children">
  <div class="abs hero-title">Pre-schools and playgroups</div>
  <div class="abs hero-sub">Lorem ipsum dolor sit amet, consectetur adipisicing elit, sed do eiusmod tempor incididunt</div>
  <div class="abs slide-arrow" style="left:25px;top:359px">
    <svg width="32" height="32"><path d="M19 10l-6 6 6 6" fill="none" stroke="#fff" stroke-width="2.5"/></svg>
  </div>
  <div class="abs slide-arrow" style="left:761px;top:359px">
    <svg width="32" height="32"><path d="M13 10l6 6-6 6" fill="none" stroke="#fff" stroke-width="2.5"/></svg>
  </div>
</section>

<div class="dropdown abs">Values<br>Mission<br>Vision<br>Purpose<br>Advantage<br>Curriculum</div>

<div class="abs crest">The Maplewick Academy</div>

<h1 class="abs welcome">Welcome to Maplewick Academy</h1>

<article class="abs card" style="left:192px">
  <div class="photo" role="img" aria-label="Photo of two girls drawing at a table" style="background:linear-gradient(135deg,#8cc66a,#e7c4b4 55%,#d85a62)"></div>
  <h3>Admissions</h3>
  <p>consectetur adipisicing elit, sed do eiusmod tempor incididunt ut labore...</p>
</article>
<article class="abs card" style="left:475px">
  <div class="photo" role="img" aria-label="Photo of two girls playing doctor with a doll" style="background:linear-gradient(135deg,#f2e6d8,#ecc7a4 50%,#e59a9a)"></div>
  <h3>Franchises</h3>
  <p>consectetur adipisicing elit, sed do eiusmod tempor incididunt ut labore...</p>
</article>
<article class="abs card" style="left:757px">
  <div class="photo" role="img" aria-label="Photo of two children playing with toys" style="background:linear-gradient(135deg,#c9a7b8,#5a7fb5 45%,#d9a23a 75%,#c24646)"></div>
  <h3>Philosophy</h3>
  <p>consectetur adipisicing elit, sed do eiusmod tempor incididunt ut labore...</p>
</article>

<section class="abs band">
  <h2>Premium child care one by one...</h2>
  <div class="abs service" style="left:192px">
    <div class="icon" style="background:var(--blue)">
      <svg width="50" height="50"><circle cx="23" cy="22" r="10" fill="none" stroke="#fff" stroke-width="3.5"/><path d="M30 29l9 9" stroke="#fff" stroke-width="4.5" stroke-linecap="round"/></svg>
    </div>
    <h4>Home School Support</h4>
    <p>Sit amet, consectetur adipisicing elit, sed do eiusmod tempor incididunt ut labore et dolore magna aliqua. Ut enim ad minim veniam, quis nostrud...</p>
    <a class="btn">Read More</a>
  </div>
  <div class="abs divider" style="left:457px"></div>
  <div class="abs service" style="left:473px">
    <div class="icon" style="background:var(--green)">
      <svg width="50" height="50"><path d="M25 9v20M17 21l8 9 8-9" fill="none" stroke="#fff" stroke-width="4"/><path d="M12 33v7h26v-7" fill="none" stroke="#fff" stroke-width="3.5"/></svg>
    </div>
    <h4>Voluntary Pre-K (VPK)</h4>
    <p>Duis aute irure dolor in reprehenderit in voluptate velit esse cillum dolore eu fugiat nulla pariatur. Excepteur sint occaecat non proident...</p>
    <a class="btn">Read More</a>
  </div>
  <div class="abs divider" style="left:738px"></div>
  <div class="abs service" style="left:759px">
    <div class="icon" style="background:var(--white)">
      <svg width="50" height="50"><path d="M8 4h24l12 12v30H8z" fill="var(--salmon)"/><path d="M32 4v12h12z" fill="#f7c1b8"/></svg>
    </div>
    <h4>Enrichment Services</h4>
    <p>Sed ut perspiciatis unde omnis iste natus error sit voluptatem accusantium doloremque laudantium, totam rem aperiam, eaque ipsa quae ab illo...</p>
    <a class="btn">Read More</a>
  </div>
</section>

<section class="abs program">
  <h2>Children from 2 – 3 Years</h2>
  <div class="call">Call us on <b>0800 555 0142</b> for more information</div>
  <div class="photo" role="img" aria-label="Photo of a teacher drawing with a group of toddlers"></div>
  <h3 style="top:338px">1. Lorem ipsum dolor sit amet,</h3>
  <p style="top:364px">consectetur adipisicing elit, sed do eiusmod tempor incididunt ut labore et dolore magna aliqua. Ut enim ad minim veniam, quis nostrud exercitation ullamco laboris nisi ut aliquip ex ea commodo consequat.</p>
  <h3 style="top:458px">2. Lorem ipsum dolor sit amet,</h3>
  <p style="top:484px">Consectetur adipisicing elit, sed do eiusmod tempor incididunt ut labore et dolore magna aliqua. Ut enim ad minim veniam, quis nostrud exercitation ullamco laboris nisi ut aliquip ex ea commodo consequat.</p>
</section>

<aside class="abs programs-menu">
  <h3>Programs</h3>
  <div class="toggle"><svg width="22" height="22"><path d="M7 9l4 4 4-4" fill="none" stroke="#777" stroke-width="2"/></svg></div>
  <ul>
    <li>Children from 1 – 2 Years</li>
    <li class="current">Children from 2 – 3 Years</li>
    <li>Children from 3 – 4 years</li>
    <li>Children from 4 - 5 Years</li>
    <li>Voluntary Pre-K (VPK)</li>
    <li>Kindergarten</li>
    <li>1st Grade</li>
    <li>2nd Grade</li>
    <li>3rd Grade</li>
    <li>4th Grade</li>
    <li>5th Grade</li>
  </ul>
</aside>

<section class="abs tabs">
  <div class="tab-bar"><span class="on">Schedule a Campus Tour</span><span>News</span><span>Contact Us</span><span>Blog</span></div>
  <div class="photo" role="img" aria-label="Photo of children at a playground picnic table"></div>
  <h4>Schedule a Campus Tour</h4>
  <p style="top:94px">Sed ut perspiciatis unde omnis iste natus error sit voluptatem accusantium doloremque laudantium, totam rem aperiam.</p>
  <p style="top:154px">Eaque ipsa quae ab illo inventore veritatis et quasi architecto beatae vitae dicta sunt explicabo. Nemo enim ipsam voluptatem quia voluptas sit aspernatur aut odit aut fugit.</p>
  <a class="abs btn" style="left:215px;top:234px">Read More</a>
</section>

<aside class="abs about">
  <h3>The Maplewick Academy</h3>
  <div class="tag">Premium child care one by one.</div>
  <div class="seal"></div>
  <h4>Letter from Principle</h4>
  <p>Sed ut perspiciatis unde omnis iste natus error sit voluptatem accusantium doloremque laudantium tore...</p>
  <a class="abs btn" style="left:88px;top:234px">Read More</a>
</aside>

<footer class="abs footer">
  <div class="photo" role="img" aria-label="Photo of children lying in a circle seen from above"></div>
  <div class="abs crest">The Maplewick Academy</div>

  <div class="abs hours">
    <b>Opening Hours<br>Reception:</b><br>Monday - Friday<br>8am - 6pm
    <svg class="ico" style="top:103px" viewBox="0 0 14 14"><path d="M7 1a4 4 0 0 1 4 4c0 3-4 8-4 8S3 8 3 5a4 4 0 0 1 4-4z" fill="#222"/><circle cx="7" cy="5" r="1.5" fill="#f2dd92"/></svg>
    <div style="margin-top:20px"><b>Contact Details</b><br>Day Care Centre,<br>18 Oakfield Lane,<br>Brandon,<br>FL 33510</div>
    <svg class="ico" style="top:223px" viewBox="0 0 14 14"><path d="M3 1l3 3-2 2a8 8 0 0 0 4 4l2-2 3 3-2 2C6 13 1 8 1 3z" fill="#222"/></svg>
    <div style="margin-top:20px"><b>Telephone:</b><br>(813) 555 0178</div>
    <svg class="ico" style="top:283px" viewBox="0 0 14 14"><path d="M1 3h12v8H1z" fill="#222"/><path d="M1 3l6 5 6-5" fill="none" stroke="#f2dd92" stroke-width="1.2"/></svg>
    <div style="margin-top:20px"><b>Email:</b><br>hello@maplewickacademy.org</div>
  </div>

  <div class="abs contact">
    <h4>Contact Us</h4>
    <p>For details on vacancies<br>please contact the Centre.</p>
    <div class="field" style="top:78px">Name</div>
    <div class="field" style="top:113px">Cell</div>
    <div class="field" style="top:149px">Email</div>
    <div class="field" style="top:185px;height:91px">Message</div>
    <div class="send">Send
      <svg style="position:absolute;left:64px;top:8px" width="12" height="12"><path d="M4 2l4 4-4 4" fill="none" stroke="#fff" stroke-width="1.5"/></svg>
    </div>
  </div>
</footer>

<div class="abs bottom">
  <div class="copy">2015 The Maplewick Academy</div>
  <div class="abs social" style="left:782px;background:#3b5998"></div>
  <div class="abs social" style="left:820px;background:#3aa9df"></div>
  <div class="abs social" style="left:857px;background:#d6443a"></div>
  <div class="abs social" style="left:894px;background:#f0892d"></div>
  <div class="abs social" style="left:978px;background:var(--blue)">
    <svg width="30" height="30"><path d="M10 18l5-5 5 5" fill="none" stroke="#fff" stroke-width="2"/></svg>
  </div>
</div>

</body>
</html>
```